Stationery Design Project

see attached logo and business card layout, envelopes, letterhead, proposal, and invoice stationery needs to all flow.

Industry/Entity Type

Business

```html
<!DOCTYPE html>
<html lang="en">
<head>
<meta charset="utf-8">
<title>Ridgeline Paving Letterhead</title>
<link href="https://fonts.googleapis.com/css2?family=Open+Sans:wght@400;600&display=swap" rel="stylesheet">
<style>
  :root {
    --backdrop: #e6e6e8;
    --paper: #ffffff;
    --band: #231f20;
    --ink: #111111;
    --brand-gold: #f2b01e;
    --brand-light: #ffffff;
    --watermark-grey: #d4d4d4;
  }
  html, body {
    margin: 0;
    padding: 0;
    width: 1200px;
    height: 1000px;
    overflow: hidden;
    background: var(--backdrop);
    font-family: "Open Sans", sans-serif;
  }
  .canvas {
    position: relative;
    width: 1200px;
    height: 1000px;
  }
  .letterhead {
    position: absolute;
    left: 237px;
    top: 20px;
    width: 726px;
    height: 960px;
    background: var(--paper);
    box-shadow: 0 4px 18px rgba(0,0,0,0.18);
    overflow: hidden;
  }
  .header-band {
    position: absolute;
    left: 0;
    top: 0;
    width: 530px;
    height: 104px;
    background: var(--band);
  }
  .brand {
    position: absolute;
    right: 30px;
    top: 38px;
    display: flex;
    align-items: center;
    gap: 10px;
  }
  .brand-dot {
    width: 14px;
    height: 14px;
    border-radius: 50%;
    background: var(--brand-gold);
  }
  .brand-name {
    font-family: "Open Sans", sans-serif;
    font-weight: 600;
    font-size: 24px;
    letter-spacing: 1px;
    color: var(--brand-light);
    text-transform: uppercase;
  }
  .letter-body {
    position: absolute;
    left: 60px;
    top: 175px;
    width: 600px;
    color: var(--ink);
    font-size: 16.5px;
    line-height: 1.2;
  }
  .letter-body p {
    margin: 0 0 22px;
    text-align: justify;
    text-align-last: center;
  }
  .letter-body .opening {
    display: block;
    text-align: center;
  }
  .watermark-name {
    position: absolute;
    left: 40px;
    top: 650px;
    display: flex;
    align-items: center;
    gap: 24px;
    color: var(--watermark-grey);
    font-weight: 600;
    font-size: 64px;
    text-transform: uppercase;
    letter-spacing: 2px;
  }
  .watermark-name .brand-dot {
    width: 54px;
    height: 54px;
    background: var(--watermark-grey);
  }
  .footer {
    position: absolute;
    left: 0;
    right: 0;
    bottom: 60px;
    text-align: center;
    color: var(--ink);
    font-size: 11px;
    line-height: 1.35;
  }
</style>
</head>
<body>
<main class="canvas">
  <article class="letterhead">
    <header class="header-band">
      <div class="brand">
        <span class="brand-dot"></span>
        <span class="brand-name">Ridgeline Paving</span>
      </div>
    </header>

    <section class="letter-body">
      <p><span class="opening">Lorem ipsum dolor sit amet, consectetur adipiscing elit.</span>
      Nam eget ante mollis libero rutrum tincidunt et quis est. Suspendisse metus velit, aliquet non rutrum eget, fermentum non dui. Morbi nisi ligula, porttitor eget accumsan ut, tincidunt ac nisi. Nunc ante enim, aliquet at sollicitudin viverra, facilisis eu mauris. Aenean et mauris non quam condimentum consequat nec ut velit. Duis non metus fermentum nibh porttitor adipiscing. Aenean libero nulla, ultricies sed porttitor vitae, condimentum sit amet risus. In sapien velit, rhoncus ut fringilla sed, egestas id dui. Nunc volutpat vestibulum consectetur. Mauris eget enim ligula, a tempus mi. Morbi felis metus, ultricies ac luctus nec, imperdiet elementum ipsum. Pellentesque non ante libero, sit amet sollicitudin odio.</p>
      <p>Nam venenatis enim ac velit varius elementum. Ut massa leo, accumsan egestas posuere quis, tempus eu nisi. Cras at justo risus, vitae pretium eros. In tempus libero et arcu bibendum eu cursus orci ornare. Donec sit amet tellus vitae augue viverra vulputate et sed leo. Donec ultrices, dui interdum commodo viverra, dolor</p>
    </section>

    <div class="watermark-name" aria-hidden="true">
      <span class="brand-dot"></span>
      <span>Ridgeline</span>
    </div>

    <footer class="footer">
      Lorem ipsum dolor sit &nbsp;Consectetur<br>
      Nam eget ante mollis libero Rutrum tinciduntSuspendisse 0987654321
    </footer>
  </article>
</main>
</body>
</html>
```